Whisker Haven Postcard - Let People Know What Animal Chiropractic Is!

I am looking for a postcard someone can look at and know why their pet needs animal chiropractic and how they can schedule the appointment. I have included the old postcard, new photos to use and logo. The contact info that needs to go on this card:

www.whiskerhaven.example
415-862-0947
assistant.drmarlow@mailbox.example

QR code - https://www.videohub.example/playlist?list=QX8m2Tb5KdRzN7pWc-Hs4Ye_LFvGUaJi3

Target Market(s)

Pet owners

Industry/Entity Type

Animal Health Care - Chiropractic

Font styles to use
Sans Serif

Requirements
Must have
• Logo, contact info, reasons for a pet needing chiropractic care, PICTURES (who doesn't love pictures)
Nice to have
• A tiny blurb on what chiropractic is for animals.
Should not have
• Empty space for an address, this card will be handed out. I do not want it to look exactly like the old one. I don't want it to be so wordy.

```html
<!DOCTYPE html>
<html lang="en">
<head>
<meta charset="utf-8">
<title>Whisker Haven Postcard</title>
<link rel="stylesheet" href="https://fonts.googleapis.com/css2?family=Barlow+Condensed:ital,wght@0,300;0,400;0,600;0,700;1,700;1,800&family=Montserrat:wght@500;700&display=swap">
<style>
:root{
  --red:#c41e2f;
  --red-deep:#9e1a26;
  --ink:#3a3a3a;
  --black:#111;
  --gray:#999b9d;
  --page:#dcdcdc;
  --white:#fff;
}
*{margin:0;padding:0;box-sizing:border-box}
html,body{width:873px;height:1200px;overflow:hidden;background:var(--page)}
body{font-family:"Barlow Condensed",sans-serif;color:var(--ink);position:relative}
.card{position:absolute;left:21px;width:831px;height:553px;background:var(--white);overflow:hidden;box-shadow:4px 5px 8px rgba(0,0,0,.25)}
.card--front{top:27px}
.card--back{top:619px}
.abs{position:absolute}

/* front */
.headline-band{left:0;top:0;width:490px;height:140px}
.headline{left:37px;top:22px;color:var(--white);font-weight:800;font-style:italic;font-size:51px;line-height:46px;letter-spacing:.2px;white-space:nowrap}
.tagline{left:37px;top:156px;color:var(--red);font-weight:700;font-style:italic;font-size:21px;line-height:23px;white-space:nowrap}
.signs-title{left:37px;top:210px;font-weight:700;font-size:19.5px;color:var(--ink);white-space:nowrap}
.signs{left:37px;top:236px;list-style:none;font-weight:300;font-size:18.5px;line-height:20.8px;color:var(--ink);width:345px}
.signs li{padding-left:9px;position:relative}
.signs li::before{content:"";position:absolute;left:0;top:9px;width:4px;height:4px;border-radius:50%;background:var(--red)}
.photo-front{left:412px;top:115px;width:419px;height:438px;
  background:
    radial-gradient(ellipse 40% 30% at 82% 28%,#e8b89a 0%,rgba(232,184,154,0) 100%),
    radial-gradient(ellipse 55% 45% at 45% 62%,#7a5a44 0%,rgba(122,90,68,0) 100%),
    linear-gradient(150deg,#f1ddd0 0%,#c79a76 30%,#8c6a4f 55%,#4a3a30 75%,#3f4a63 100%);
  clip-path:polygon(70% 0,100% 0,100% 100%,8% 100%,0 68%,6% 45%,20% 30%,45% 22%,62% 12%)}
.brand{left:469px;top:36px;width:200px;text-align:center}
.brand__mark{width:148px;height:148px;margin:0 auto 14px;border-radius:50%;border:9px solid var(--red)}
.brand__name{font-family:"Montserrat",sans-serif;font-weight:700;font-size:16.5px;color:var(--black);letter-spacing:.4px;line-height:20px;white-space:nowrap}
.brand__sub{font-family:"Montserrat",sans-serif;font-weight:500;font-size:8.2px;color:var(--red);letter-spacing:.9px;margin-top:2px;white-space:nowrap}
.badge{left:667px;top:370px;width:100px;height:100px;border-radius:50%;background:var(--red);border:6px solid var(--white);box-shadow:0 0 0 3px var(--red)}
.contact-bar{left:0;top:502px;width:831px;height:35px}
.contact-bar span{position:absolute;top:4px;color:var(--white);font-weight:700;font-size:18.5px;white-space:nowrap}

/* back */
.red-panel{left:0;top:0;width:397px;height:553px;
  background:
    radial-gradient(ellipse 45% 35% at 75% 30%,rgba(240,110,110,.45) 0%,rgba(240,110,110,0) 100%),
    linear-gradient(160deg,#b3232e 0%,#d2373f 40%,#a5212c 70%,var(--red-deep) 100%)}
.about{left:44px;top:34px;width:236px;color:var(--white);font-weight:300;font-size:17.8px;line-height:21.2px}
.about strong{font-weight:700}
.about p+p{margin-top:21px}
.photo-octagon{left:307px;top:38px;width:184px;height:188px;background:var(--white);clip-path:polygon(29% 0,71% 0,100% 29%,100% 71%,71% 100%,29% 100%,0 71%,0 29%)}
.photo-octagon div{position:absolute;inset:4px;
  background:
    radial-gradient(ellipse 35% 30% at 50% 40%,#e9dfd3 0%,rgba(233,223,211,0) 100%),
    linear-gradient(170deg,#2b2522 0%,#5a4436 35%,#d8ccc0 65%,#3a3430 100%);
  clip-path:polygon(29% 0,71% 0,100% 29%,100% 71%,71% 100%,29% 100%,0 71%,0 29%)}
.photo-cart{left:275px;top:245px;width:340px;height:308px;
  background:
    radial-gradient(ellipse 35% 35% at 45% 45%,#f6f1e8 0%,rgba(246,241,232,0) 100%),
    linear-gradient(175deg,#efe8dc 0%,#e3d8c8 45%,#e3b2c2 68%,#5a5a5a 85%,#2c2c2c 100%);
  clip-path:polygon(30% 4%,45% 0,68% 6%,72% 30%,88% 44%,100% 70%,100% 100%,0 100%,6% 70%,25% 40%,20% 20%)}
.schedule{left:460px;top:99px;width:415px;text-align:center}
.schedule .council{font-weight:700;font-size:20px;line-height:23px;color:var(--ink)}
.schedule .cta{font-weight:700;font-size:20px;color:var(--red);line-height:24px}
.schedule .ask{font-weight:700;font-size:20px;color:var(--ink);margin-top:16px}
.schedule .phone{font-weight:700;font-size:46px;line-height:44px;color:var(--red);margin-top:2px}
.schedule .email{font-weight:700;font-size:18px;color:var(--ink);line-height:22px;margin-top:2px}
.schedule .web{font-weight:700;font-size:19px;color:var(--red);line-height:23px}
.brand--back{left:606px;top:357px;width:200px}
.brand--back .brand__mark{width:128px;height:128px;border-width:8px;margin-bottom:9px}
.brand--back .brand__name{font-size:14.5px}
.brand--back .brand__sub{font-size:7.2px}
</style>
</head>
<body>

<section class="card card--front">
  <svg class="abs headline-band" viewBox="0 0 490 140" width="490" height="140" aria-hidden="true">
    <polygon points="0,0 474,0 422,140 0,140" fill="var(--gray)"/>
    <polygon points="0,0 463,0 416,130 0,130" fill="var(--red)"/>
  </svg>
  <h1 class="abs headline">CHIROPRACTIC CARE<br>FOR YOUR PET!</h1>

  <div class="abs photo-front" role="img" aria-label="Photo of the chiropractor smiling while holding a fawn French bulldog close to her face"></div>

  <div class="abs brand">
    <div class="brand__mark"></div>
    <div class="brand__name">DR. ELENA MARLOW</div>
    <div class="brand__sub">ANIMAL AND HUMAN CHIROPRACTOR</div>
  </div>

  <div class="abs badge" role="img" aria-label="Certification seal"></div>

  <p class="abs tagline">DR. ELENA MARLOW, CHIROPRACTOR, WHO HAS BEEN<br>PROVIDING CHIROPRACTIC CARE FOR OVER 15 YEARS!</p>
  <h2 class="abs signs-title">Why does my pet need chiropractic - signs/symptoms</h2>
  <ul class="abs signs">
    <li>A limp that will not go away</li>
    <li>Yelping in pain with sudden movement</li>
    <li>Resists jumping in, out or on things as much</li>
    <li>Diagnosed with disc disease</li>
    <li>Wellness (Prevention) - a well moving spine will help prevent arthritis later in life</li>
    <li>Rehab for sprain/strain, surgery</li>
    <li>Athletics - flyball, agility, show dogs - top athletes receive regular chiropractic care</li>
    <li>Working Animals - Police, service</li>
    <li>Sudden change in behavior that is unexplained</li>
    <li>Hip pain</li>
  </ul>

  <div class="abs contact-bar">
    <svg class="abs" viewBox="0 0 831 35" width="831" height="35" style="left:0;top:0" aria-hidden="true">
      <rect x="0" y="0" width="324" height="35" fill="var(--gray)"/>
      <polygon points="320,0 585,0 576,35 314,35" fill="var(--black)"/>
      <polygon points="585,0 831,0 831,35 576,35" fill="var(--red)"/>
    </svg>
    <span style="left:35px">Location by Appointment: 415-862-0947</span>
    <span style="left:334px;font-size:15.5px;top:6px">assistant.drmarlow@mailbox.example</span>
    <span style="left:605px;font-size:18px">www.whiskerhaven.example</span>
  </div>
</section>

<section class="card card--back">
  <div class="abs red-panel" role="img" aria-label="Red-toned photo of the chiropractor with a horse"></div>
  <div class="abs about">
    <p><strong>WHAT IS CHIROPRACTIC</strong> - in simplest terms, a conservative approach to healthcare. We focus on the movement in the joints (spine/extremities) for the overall health and wellness of the pet. Restrictions in joint motion, can affect such things as athletic performance, normal biomechanics leading to repetitive stress injuries and sprain/ strains. The issue, most restrictions in joint motions are subclinical and go undetected until they manifest into a problem.</p>
    <p>Animal chiropractic adjustments are not only for pets with injuries, it's great to start young so that we know how the spine / extremities are moving prior to a problem. Chiropractic adjustments definitely help with new and existing injuries. We also offer low level laser treatments to assist in the healing process.</p>
  </div>

  <div class="abs photo-octagon" role="img" aria-label="Photo of a long-haired chihuahua wearing a striped tie"><div></div></div>
  <div class="abs photo-cart" role="img" aria-label="Photo of a white French bulldog in a pink mobility cart"></div>

  <div class="abs schedule">
    <div class="council">Global Animal<br>Chiropractic Council</div>
    <div class="cta">Schedule an appointment today!</div>
    <div class="ask">PLEASE CALL, TEXT OR EMAIL US.</div>
    <div class="phone">415-862-0947</div>
    <div class="email">assistant.drmarlow@mailbox.example</div>
    <div class="web">www.whiskerhaven.example</div>
  </div>

  <div class="abs brand brand--back">
    <div class="brand__mark"></div>
    <div class="brand__name">DR. ELENA MARLOW</div>
    <div class="brand__sub">ANIMAL AND HUMAN CHIROPRACTOR</div>
  </div>
</section>

</body>
</html>
```